WordPress Website for Accounting Firm

I have attached an excel sheet showing what i need done for my accounting website. Currently i have a WP website but its not live and do not like it. I can give a link if that will help. Total pages is around 12. I can buy and supply the images but have provided indication of what i want in the excel. I will need the designer to do the coding to make the website fully functional. I want a clean look and attractive. Don't want too dark colors. Once i like the landing page, i will need the designer to code code the website. Just want to look first. I will provide the logo file and put the contents myself. Just put dummy contents for now to show how it will look.
Updates
Can you please use the attached images so i can see how nit will look on the coverage as an option. These are from pixelharbor
264918053
418273596
1537206419
1096382147
Currently there are only 2 provided by myself as Photo 1 and Photo 2
Many Thanks!
Industry/Entity Type
Accounting and Finance
Number of Pages Required
5+ page

```html
<!DOCTYPE html>
<html lang="en">
<head>
<meta charset="utf-8">
<title>Ledgerwell – Tax &amp; Accounting</title>
<link href="https://fonts.googleapis.com/css2?family=League+Spartan:wght@400;600;700&family=Jost:wght@400;500&display=swap" rel="stylesheet">
<style>
:root{
  --green:#4f9a3f;
  --green-dark:#3f8a31;
  --green-pale:#e9f2e8;
  --off-white:#f4f6f3;
  --ink:#1b1b1b;
  --text:#444;
  --white:#fff;
}
*{box-sizing:border-box;margin:0;padding:0}
html,body{width:1200px;height:3071px;overflow:hidden}
body{position:relative;background:var(--white);font-family:"Jost",sans-serif;color:var(--ink)}
.abs{position:absolute}
.btn{position:absolute;display:flex;align-items:center;justify-content:center;background:var(--green);color:var(--white);border-radius:22px;font-family:"Jost",sans-serif;font-size:17px}

/* header */
.site-header{left:0;top:0;width:1200px;height:67px;background:var(--off-white)}
.brand{display:flex;align-items:center;gap:8px;font-family:"Jost",sans-serif;font-weight:500;font-size:20px;color:var(--green)}
.brand-dot{width:14px;height:14px;border-radius:50%;background:var(--green)}
.site-header .brand{left:116px;top:20px}
.nav{left:546px;top:26px;display:flex;gap:0;font-size:13px;font-weight:500}
.nav a{position:absolute;white-space:nowrap;color:var(--ink);text-decoration:none}
.nav .active{border-bottom:2px solid var(--green);padding-bottom:3px}
.btn-contact{left:961px;top:17px;width:124px;height:33px;font-size:13px;font-weight:500;border-radius:17px}

/* hero */
.hero{left:0;top:67px;width:1200px;height:660px}
.hero-title{left:161px;top:222px;font-family:"League Spartan",sans-serif;font-weight:700;font-size:86px;line-height:78px;color:var(--white)}
.hero-sub{left:161px;top:402px;font-size:29px;color:var(--white);font-weight:400}
.btn-hero{left:160px;top:467px;width:136px;height:38px}
.hero-next{left:1048px;top:326px;width:48px;height:48px;border-radius:50%;background:var(--green)}
.scroll-cue{left:562px;top:675px;width:76px;height:76px;border-radius:50%;background:var(--white);border:2px solid #e2e2e2;box-shadow:0 2px 8px rgba(0,0,0,.1)}

/* about */
.about{left:0;top:715px;width:1200px;height:513px;background:var(--off-white);z-index:-1}
.about-media{left:159px;top:781px;width:336px;height:385px;border-radius:26px;background:linear-gradient(180deg,#8dbbe0 0%,#e9b478 22%,#7a9a4a 55%,#8a6a52 85%,#6d655b 100%)}
.section-title{font-family:"League Spartan",sans-serif;font-weight:700;font-size:45px;color:var(--ink);line-height:1}
.section-title .light{font-weight:400}
.rule{height:3px;width:54px;background:var(--green)}
.lead{font-size:16.5px;color:var(--ink)}
.body-copy{font-size:13.5px;line-height:24.5px;color:var(--text)}

/* why */
.why{left:0;top:1228px;width:1200px;height:590px;background:var(--green-pale)}
.checks{list-style:none;font-size:15px;line-height:23px;color:var(--text)}
.checks li{position:absolute;padding-left:26px;white-space:nowrap}
.tick{position:absolute;left:0;top:4px;width:14px;height:14px}

/* testimonials */
.divider{left:579px;top:1903px;width:1px;height:318px;background:#cfcfcf}
.hand{border-radius:40px;background:linear-gradient(160deg,#f3cdb0,#d9a07c)}
.wordmark{left:200px;top:2004px;width:240px;text-align:center;font-family:"League Spartan",sans-serif;font-weight:700;font-size:38px;line-height:37px;color:#2b2b2b}
.wordmark .accent{color:var(--green)}
.avatar{left:813px;top:1912px;width:96px;height:96px;border-radius:50%;border:3px solid var(--green);background:linear-gradient(160deg,#f0a365,#7a4b36)}
.quote{left:659px;top:2030px;width:410px;text-align:center;font-size:11.5px;line-height:21px;color:var(--text)}
.qmark{font-family:"League Spartan",sans-serif;font-weight:700;font-size:34px;color:var(--ink)}
.dots{left:843px;top:2196px;display:flex;gap:5px}
.dots span{width:9px;height:9px;border-radius:50%;background:var(--green)}
.dots .off{background:var(--white);border:1.5px solid var(--green)}

/* industries */
.industries{left:0;top:2306px;width:1200px;height:492px;background:var(--off-white)}
.card{width:202px;height:170px;background:var(--white);border-radius:6px;box-shadow:0 2px 14px rgba(0,0,0,.05)}
.card.tint{background:var(--green-pale)}
.card ul{list-style:none;font-size:12.5px;color:var(--ink)}
.card li{position:absolute;left:26px;padding-left:24px;white-space:nowrap}

/* footer */
.site-footer{left:0;top:2798px;width:1200px;height:273px;background:var(--green);color:var(--white)}
.site-footer .brand{color:var(--white);font-size:22px}
.site-footer .brand-dot{background:var(--white)}
.foot-col h4{font-family:"Jost",sans-serif;font-weight:500;font-size:15.5px;margin-bottom:10px}
.foot-col a{display:block;color:var(--white);text-decoration:none;font-size:11px;line-height:19.5px;text-transform:uppercase}
.social{display:flex;gap:22px}
.social span{width:18px;height:18px;border-radius:50%;border:2px solid var(--white)}
.legal{font-size:12px}
</style>
</head>
<body>

<header class="site-header abs">
  <div class="brand abs"><span class="brand-dot"></span>Ledgerwell</div>
  <nav class="nav abs">
    <a class="active" style="left:0">HOME</a>
    <a style="left:69px">SOLUTIONS</a>
    <a style="left:174px">CLIENTS</a>
    <a style="left:259px">CLIENT RESOURSES</a>
  </nav>
  <a class="btn btn-contact">CONTACT US</a>
</header>

<section class="hero abs">
  <svg width="1200" height="660" viewBox="0 0 1200 660" class="abs" style="left:0;top:0">
    <defs>
      <radialGradient id="heroPhoto" cx="0.5" cy="0.45" r="0.7">
        <stop offset="0" stop-color="#e7a55a"/>
        <stop offset="0.22" stop-color="#5a7fa6"/>
        <stop offset="0.45" stop-color="#3c5f7d"/>
        <stop offset="0.7" stop-color="#6b4126"/>
        <stop offset="1" stop-color="#2a1a12"/>
      </radialGradient>
    </defs>
    <path role="img" aria-label="Climber on a sea cliff cave at sunset" d="M0 0H1200V592Q640 690 0 590Z" fill="url(#heroPhoto)"/>
    <path d="M0 590Q600 690 1200 592" fill="none" stroke="#4f9a3f" stroke-width="7"/>
    <rect y="655" width="1200" height="5" fill="#f4f6f3"/>
  </svg>
  <h1 class="hero-title abs">Tax &amp;<br>Accounting</h1>
  <p class="hero-sub abs">Services for a Variety of Industries.</p>
  <a class="btn btn-hero">Learn More</a>
  <div class="hero-next abs">
    <svg width="48" height="48" viewBox="0 0 48 48"><path d="M20 15l9 9-9 9" fill="none" stroke="#1b1b1b" stroke-width="3.5" stroke-linecap="round"/></svg>
  </div>
</section>

<div class="scroll-cue abs">
  <svg width="72" height="72" viewBox="0 0 72 72"><rect x="30" y="20" width="12" height="20" rx="6" fill="none" stroke="#1b1b1b" stroke-width="1.6"/><line x1="36" y1="25" x2="36" y2="30" stroke="#1b1b1b" stroke-width="1.6"/><path d="M32 44l4 4 4-4M32 49l4 4 4-4" fill="none" stroke="#1b1b1b" stroke-width="1.6"/></svg>
</div>

<section class="about abs"></section>
<div class="about-media abs" role="img" aria-label="Coastal landscape photograph"></div>
<h2 class="section-title abs" style="left:597px;top:835px">About <span class="light">Us</span></h2>
<p class="lead abs" style="left:597px;top:885px">Lorem Ipsum is simply dummy text of the printing.</p>
<div class="rule abs" style="left:597px;top:914px"></div>
<p class="body-copy abs" style="left:597px;top:938px;width:450px">Lorem Ipsum is simply dummy text of the printing and typesetting industry. Lorem Ipsum has been the industry's standard dummy text ever since the 1500s, when an unknown printer took a galley of type and scrambled it to make a type specimen book. It has survived not only five centuries,</p>
<p class="body-copy abs" style="left:597px;top:1051px;width:450px;color:var(--ink)">Lorem Ipsum is simply dummy text of the printing and typesetting industry. Lorem Ipsum has been the industry's standard dummy text</p>

<section class="why abs">
  <svg width="1200" height="590" class="abs" style="left:0;top:0">
    <circle cx="905" cy="140" r="82" fill="#4f9a3f"/>
    <ellipse cx="905" cy="340" rx="200" ry="150" fill="#cfe3ca"/>
  </svg>
  <h2 class="section-title abs" style="left:123px;top:138px">WHY <span class="light">CHOOSE Us</span></h2>
  <div class="rule abs" style="left:123px;top:192px"></div>
  <ul class="checks">
    <li style="left:116px;top:229px"><svg class="tick" viewBox="0 0 14 14"><circle cx="7" cy="7" r="7" fill="#4f9a3f"/><path d="M4 7.2l2 2 4-4" fill="none" stroke="#fff" stroke-width="1.6"/></svg>We specialise in accounting and tax solutions for all business<br>structures and industries</li>
    <li style="left:116px;top:289px"><svg class="tick" viewBox="0 0 14 14"><circle cx="7" cy="7" r="7" fill="#4f9a3f"/><path d="M4 7.2l2 2 4-4" fill="none" stroke="#fff" stroke-width="1.6"/></svg>Our team are qualified professionals with 50+ years of combined<br>experience in CA industry</li>
    <li style="left:116px;top:349px"><svg class="tick" viewBox="0 0 14 14"><circle cx="7" cy="7" r="7" fill="#4f9a3f"/><path d="M4 7.2l2 2 4-4" fill="none" stroke="#fff" stroke-width="1.6"/></svg>We are Accessable 7 days a week</li>
    <li style="left:116px;top:386px"><svg class="tick" viewBox="0 0 14 14"><circle cx="7" cy="7" r="7" fill="#4f9a3f"/><path d="M4 7.2l2 2 4-4" fill="none" stroke="#fff" stroke-width="1.6"/></svg>We constantly upskill to keep up with changes to tax laws and legislation</li>
  </ul>
  <a class="btn" style="left:116px;top:438px;width:137px;height:39px">Learn More</a>
  <div class="abs" role="img" aria-label="Woman using a phone among digital data overlays" style="left:715px;top:99px;width:370px;height:369px;border-radius:22px;background:linear-gradient(135deg,#2f5f84 0%,#7b5a6a 45%,#e08a3a 80%,#f4a63b 100%)"></div>
</section>

<div class="divider abs"></div>
<div class="hand abs" role="img" aria-label="Hand making an OK gesture" style="left:101px;top:1951px;width:125px;height:159px"></div>
<div class="hand abs" role="img" aria-label="Hand making an OK gesture" style="left:405px;top:1979px;width:125px;height:173px"></div>
<div class="wordmark abs">Don’t take<br><span class="accent">our word</span><br>for it</div>
<div class="avatar abs" role="img" aria-label="Client portrait"></div>
<span class="qmark abs" style="left:643px;top:2000px">“</span>
<p class="quote abs">Lorem Ipsum is simply dummy text of the printing and typesetting industry. Lorem Ipsum has been the industry's standard dummy text ever since the 1500s, when an unknown printer took a galley of type and scrambled it to make a type specimen book. It has survived not only five centuries, but also the leap into electronic typesetting, remaining essentially unchanged.</p>
<span class="qmark abs" style="left:1026px;top:2122px">”</span>
<p class="abs" style="left:838px;top:2145px;font-size:13.5px">Jon Doe</p>
<div class="dots abs"><span></span><span class="off"></span><span></span></div>

<section class="industries abs">
  <h2 class="section-title abs" style="left:0;width:1200px;text-align:center;top:83px">Industries We <span class="light">Represent</span></h2>
  <p class="lead abs" style="left:0;width:1200px;text-align:center;top:137px">Lorem Ipsum is simply dummy text of the printing.</p>
  <div class="rule abs" style="left:573px;top:170px"></div>

  <div class="card abs" style="left:148px;top:210px"><ul>
    <li style="top:33px"><svg class="tick" viewBox="0 0 14 14"><circle cx="7" cy="7" r="7" fill="#4f9a3f"/><path d="M4 7.2l2 2 4-4" fill="none" stroke="#fff" stroke-width="1.6"/></svg>Healthcare Specialists</li>
    <li style="top:70px"><svg class="tick" viewBox="0 0 14 14"><circle cx="7" cy="7" r="7" fill="#4f9a3f"/><path d="M4 7.2l2 2 4-4" fill="none" stroke="#fff" stroke-width="1.6"/></svg>Contractors</li>
    <li style="top:107px"><svg class="tick" viewBox="0 0 14 14"><circle cx="7" cy="7" r="7" fill="#4f9a3f"/><path d="M4 7.2l2 2 4-4" fill="none" stroke="#fff" stroke-width="1.6"/></svg>Manufacturing</li>
  </ul></div>
  <div class="card tint abs" style="left:381px;top:210px"><ul>
    <li style="top:33px"><svg class="tick" viewBox="0 0 14 14"><circle cx="7" cy="7" r="7" fill="#4f9a3f"/><path d="M4 7.2l2 2 4-4" fill="none" stroke="#fff" stroke-width="1.6"/></svg>Healthcare Specialists</li>
    <li style="top:70px"><svg class="tick" viewBox="0 0 14 14"><circle cx="7" cy="7" r="7" fill="#4f9a3f"/><path d="M4 7.2l2 2 4-4" fill="none" stroke="#fff" stroke-width="1.6"/></svg>Contractors</li>
    <li style="top:107px"><svg class="tick" viewBox="0 0 14 14"><circle cx="7" cy="7" r="7" fill="#4f9a3f"/><path d="M4 7.2l2 2 4-4" fill="none" stroke="#fff" stroke-width="1.6"/></svg>Manufacturing</li>
  </ul></div>
  <div class="card abs" style="left:616px;top:210px"><ul>
    <li style="top:33px"><svg class="tick" viewBox="0 0 14 14"><circle cx="7" cy="7" r="7" fill="#4f9a3f"/><path d="M4 7.2l2 2 4-4" fill="none" stroke="#fff" stroke-width="1.6"/></svg>Healthcare Specialists</li>
    <li style="top:70px"><svg class="tick" viewBox="0 0 14 14"><circle cx="7" cy="7" r="7" fill="#4f9a3f"/><path d="M4 7.2l2 2 4-4" fill="none" stroke="#fff" stroke-width="1.6"/></svg>Contractors</li>
    <li style="top:107px"><svg class="tick" viewBox="0 0 14 14"><circle cx="7" cy="7" r="7" fill="#4f9a3f"/><path d="M4 7.2l2 2 4-4" fill="none" stroke="#fff" stroke-width="1.6"/></svg>Manufacturing</li>
  </ul></div>
  <div class="card abs" style="left:850px;top:210px"><ul>
    <li style="top:33px"><svg class="tick" viewBox="0 0 14 14"><circle cx="7" cy="7" r="7" fill="#4f9a3f"/><path d="M4 7.2l2 2 4-4" fill="none" stroke="#fff" stroke-width="1.6"/></svg>Healthcare Specialists</li>
    <li style="top:70px"><svg class="tick" viewBox="0 0 14 14"><circle cx="7" cy="7" r="7" fill="#4f9a3f"/><path d="M4 7.2l2 2 4-4" fill="none" stroke="#fff" stroke-width="1.6"/></svg>Contractors</li>
    <li style="top:107px"><svg class="tick" viewBox="0 0 14 14"><circle cx="7" cy="7" r="7" fill="#4f9a3f"/><path d="M4 7.2l2 2 4-4" fill="none" stroke="#fff" stroke-width="1.6"/></svg>Manufacturing</li>
  </ul></div>
</section>

<footer class="site-footer abs">
  <div class="brand abs" style="left:159px;top:58px"><span class="brand-dot"></span>Ledgerwell</div>
  <div class="social abs" style="left:166px;top:134px"><span></span><span></span><span></span><span></span></div>
  <div class="foot-col abs" style="left:440px;top:47px">
    <h4>Solutions</h4>
    <a>Tax and Accounting</a><a>Cloud Accounting</a><a>Specialist</a>
  </div>
  <div class="foot-col abs" style="left:665px;top:47px">
    <h4>Clients</h4>
    <a>What Clients Say</a><a>Client Reward Scheme</a><a>Industries We Represent</a>
  </div>
  <div class="foot-col abs" style="left:910px;top:47px">
    <h4>Clients</h4>
    <a>Newsletters</a><a>Web Links</a><a>Compliance Documents</a>
  </div>
  <p class="legal abs" style="left:164px;top:228px">Copyright @ Ledgerwell &nbsp;|&nbsp; All Rights Reserved.</p>
  <p class="legal abs" style="left:919px;top:228px">Home &nbsp;&nbsp;&nbsp;| &nbsp;&nbsp;&nbsp;Contact Us</p>
</footer>

</body>
</html>
```